Label for a bottle of Gin soon to launch in the UK.

We need a label for a gin called Halworth Gin. It is very important that the label does not infringe any copyrights of the football club so please avoid the colour blue or anything related to football or the club. The example bottle below shows the bottle that we will be using. The gin will be clear not pink, the use of gold on the label is encouraged.
Should not infringe on the brand shown in the example image.

Club

Sans Serif

• Here is a link to the bottle that the label must fit onto https://www.flaskcrate-depot.co.uk/Glass-bottles/Glass-bottles/700ml-glass-bottles/700ml-clear-glass-bottle-Marosa.html
• No use of blue or anything related to football or Halworth Football Club or Moorhawks. Avoid Red also. White, gold and black should be primary colours used

```html
<!DOCTYPE html>
<html lang="en">
<head>
<meta charset="utf-8">
<title>Halworth Gin – Label</title>
<link rel="stylesheet" href="https://fonts.googleapis.com/css2?family=Jost:wght@400;500;600&display=swap">
<style>
  :root {
    --backdrop: #ecebe6;
    --label-white: #f7f7f5;
    --ink: #161616;
    --gold: #c9a23a;
    --pattern-tone: #ececea;
    --muted: #4a4a4a;
  }
  * { box-sizing: border-box; margin: 0; padding: 0; }
  html, body {
    width: 1036px;
    height: 1200px;
    overflow: hidden;
    background: var(--backdrop);
    font-family: "Jost", sans-serif;
  }
  .canvas {
    position: relative;
    width: 1036px;
    height: 1200px;
  }

  /* Neck label */
  .neck-label {
    position: absolute;
    left: 443px;
    top: 50px;
    width: 150px;
    height: 290px;
    background: var(--ink);
    overflow: hidden;
  }
  .neck-label__lines {
    position: absolute;
    inset: 0;
  }
  .neck-label__name {
    position: absolute;
    left: 50%;
    top: 50%;
    transform: translate(-50%, -50%) rotate(-90deg);
    color: #ffffff;
    font-weight: 500;
    font-size: 44px;
    letter-spacing: 3px;
    white-space: nowrap;
    background: var(--ink);
    padding: 0 10px;
    line-height: 1;
  }
  .neck-label__sub {
    position: absolute;
    left: 70px;
    bottom: 8px;
    transform-origin: left bottom;
    transform: rotate(-90deg) translate(0, 30px);
    color: #ffffff;
    font-weight: 400;
    font-size: 18px;
    letter-spacing: 1px;
    line-height: 1;
  }

  /* Front label */
  .front-label {
    position: absolute;
    left: 118px;
    top: 390px;
    width: 800px;
    height: 640px;
    background: var(--label-white);
  }
  .front-label__frame {
    position: absolute;
    inset: 6px;
    border: 2px solid var(--gold);
  }
  .front-label__pattern {
    position: absolute;
    left: 105px;
    top: 40px;
    width: 590px;
    height: 560px;
    background: radial-gradient(ellipse at center, var(--pattern-tone) 0%, var(--label-white) 75%);
  }
  .brand-mark {
    position: absolute;
    left: 0;
    right: 0;
    top: 90px;
    display: flex;
    align-items: center;
    justify-content: center;
    gap: 18px;
  }
  .brand-mark__square {
    width: 56px;
    height: 56px;
    background: var(--ink);
  }
  .brand-mark__name {
    color: var(--ink);
    font-weight: 500;
    font-size: 30px;
    letter-spacing: 2px;
  }
  .wordmark {
    position: absolute;
    left: 0;
    right: 0;
    top: 322px;
    text-align: center;
    color: var(--ink);
  }
  .wordmark__name {
    display: block;
    font-weight: 600;
    font-size: 74px;
    letter-spacing: 4px;
    line-height: 1;
  }
  .wordmark__type {
    display: block;
    margin-top: 10px;
    font-weight: 400;
    font-size: 40px;
    letter-spacing: 2px;
    line-height: 1;
  }
  .spec-line {
    position: absolute;
    left: 137px;
    width: 526px;
    top: 560px;
    height: 36px;
    border-top: 1px solid #9a9a9a;
    border-bottom: 1px solid #9a9a9a;
    display: flex;
    align-items: center;
    justify-content: space-between;
    padding: 0 10px;
    color: var(--muted);
    font-size: 20px;
    letter-spacing: 1px;
  }
  .spec-line__divider {
    width: 1px;
    height: 22px;
    background: #9a9a9a;
  }
</style>
</head>
<body>
  <main class="canvas">
    <section class="neck-label" aria-label="Neck label">
      <svg class="neck-label__lines" width="150" height="290" viewBox="0 0 150 290" aria-hidden="true">
        <polyline points="0,30 75,70 150,30" fill="none" stroke="#c9a23a" stroke-width="1.5"/>
        <line x1="75" y1="70" x2="75" y2="290" stroke="#c9a23a" stroke-width="1.5"/>
      </svg>
      <span class="neck-label__name">HALWORTH</span>
      <span class="neck-label__sub">GIN</span>
    </section>

    <section class="front-label" aria-label="Front label">
      <div class="front-label__pattern" role="img" aria-label="Faint light-grey interlocking geometric pattern behind the name"></div>
      <div class="front-label__frame"></div>

      <div class="brand-mark">
        <span class="brand-mark__square"></span>
        <span class="brand-mark__name">HALWORTH GIN</span>
      </div>

      <h1 class="wordmark">
        <span class="wordmark__name">HALWORTH</span>
        <span class="wordmark__type">GIN</span>
      </h1>

      <div class="spec-line">
        <span class="spec-line__abv">40% ALC/VOL</span>
        <span class="spec-line__divider"></span>
        <span class="spec-line__volume">500 ML</span>
      </div>
    </section>
  </main>
</body>
</html>
```